Business Card Design- Mortgage Firm

Looking to design a business Card for our Outside sales people. This card is used to provide their contact information to prospective clients and realtors. Must have All Pertinent company and licensing information by law. We are looking for a very modern design that flows with our current logo color scheme. Red/White/Black

Industry/Entity Type

Mortgage Lender

Contact Information for Business Card

Must stick with current color scheme.

Colors
f04a50
ffffff
ecf7fb

Requirements
Must have
• Company Logo or similar
• Company Address (748 W Alder Avenue, Suite 312, Corona CA 92879 NMLS: 4072916)
• Agent Name (Mira Talbot)
• Title (Senior Mortgage Loan Originator)
• NMLS# 8395021
• Toll Free: 800-627-3184
• Direct : 310-555-4860
Nice to have
• Room for Agent Picture

```html
<!DOCTYPE html>
<html lang="en">
<head>
<meta charset="utf-8">
<title>Bravina Mortgage – Business Card</title>
<link rel="stylesheet" href="https://fonts.googleapis.com/css2?family=Montserrat:wght@400;500;600&display=swap">
<style>
  :root {
    --page: #f4f5f6;
    --card: #e8eced;
    --red: #b81f26;
    --ink: #141414;
    --white: #ffffff;
  }
  * { margin: 0; padding: 0; box-sizing: border-box; }
  html, body {
    width: 1200px; height: 1076px; overflow: hidden;
    background: var(--page);
    font-family: "Montserrat", sans-serif;
  }
  .card {
    position: absolute; left: 100px; top: 252px;
    width: 1000px; height: 572px;
    background: var(--card);
    box-shadow: 0 10px 30px rgba(0,0,0,.12);
    overflow: hidden;
  }
  .sweep { position: absolute; left: 0; top: 0; width: 1000px; height: 200px; }
  .brand {
    position: absolute; left: 330px; top: 58px; width: 400px;
    display: flex; align-items: center; gap: 12px;
  }
  .brand-square { width: 24px; height: 24px; background: var(--red); flex: none; }
  .brand-name {
    font-weight: 600; font-size: 28px; letter-spacing: 2px;
    color: var(--red); text-transform: uppercase; white-space: nowrap;
  }
  .agent-name {
    position: absolute; left: 60px; top: 170px;
    font-weight: 600; font-size: 104px; line-height: 1;
    color: var(--ink); letter-spacing: -1px; white-space: nowrap;
  }
  .agent-title {
    position: absolute; left: 64px; top: 290px;
    font-weight: 500; font-size: 34px; color: var(--ink); white-space: nowrap;
  }
  .contact {
    position: absolute; left: 68px; top: 352px;
    list-style: none; font-size: 21px; line-height: 36px; color: var(--ink);
  }
  .photo-frame {
    position: absolute; left: 705px; top: 110px;
    width: 230px; height: 230px;
    border: 6px solid var(--red);
    display: flex; align-items: center; justify-content: center;
    text-align: center;
    font-weight: 500; font-size: 34px; line-height: 1.15; color: var(--ink);
  }
  .address-band {
    position: absolute; left: 0; bottom: 0;
    width: 100%; height: 64px; background: var(--red);
    display: flex; align-items: center; justify-content: flex-end;
    padding: 0 36px;
    color: var(--white); font-weight: 500; font-size: 19px; white-space: nowrap;
  }
</style>
</head>
<body>
  <article class="card">
    <svg class="sweep" viewBox="0 0 1000 200" aria-hidden="true">
      <polygon points="20,150 310,96 310,101" fill="var(--red)"/>
      <polygon points="760,66 990,26 990,30 760,72" fill="var(--red)"/>
    </svg>

    <div class="brand">
      <span class="brand-square"></span>
      <span class="brand-name">Bravina Mortgage</span>
    </div>

    <h1 class="agent-name">Mira Talbot</h1>
    <p class="agent-title">Senior Mortgage Loan Originator</p>
    <ul class="contact">
      <li>NMLS# 8395021</li>
      <li>Toll Free: 800-627-3184</li>
      <li>Direct : 310-555-4860</li>
    </ul>

    <div class="photo-frame" role="img" aria-label="Space for the agent's portrait photo">Agent<br>Picture</div>

    <footer class="address-band">Company Address: 748 W Alder Avenue, Suite 312, Corona CA 92879 &nbsp;|&nbsp; NMLS: 4072916</footer>
  </article>
</body>
</html>
```